Corporate services company needs a brochure

We are starting a company offering setup services to companies new to that location.
This includes services such as recruitment, company formation, advertising, marketing, pr, handling legal issues, logistics, transportation, procurement,immigration services, corporate gifts, accomodation,entertainment, training, administrative services etc.
Basically taking the setup issues off the hands of the company allowing them focus on their core business.

We are looking to design a professional brochure which would give the potential customers the confidence to entrust us with their needs.

We will be including some copy that can be used but i would very much like for you to bring what i have written to life - adding, deducting and amending where required.

We are looking at a A4 4/6 paged brochure but open to suggestions.

                                       

If you have any images that are suitable, please let us know. We will also be searching for some to add.

The first prize has been increased.

Thanks

Reason: We have just guaranteed the payment and we are hoping that this will encourage good designers to participate.

Reason: Some designers have requested more time to complete their final design.

Hi, I h extended the deadline to give designers more time to work on designs.

we are also looking at making the brochure a height of 8.5 and a width of 11. Please let me know your thoughts on this as any advice will help. The whole objective is to make it look as up to date and creative as possible. There is also another design size of 7.5 by 8.5

Thanks

                                        Hi

The copy has been revised and uploaded.

Hopefully it will give a clearer explanation of what we are trying to do.

Please let me know if you have any further questions.

Thanks

Mabel

Reason: adding finishing touches to designs

Reason: We are amending the copy for the brochure

Reason: The new copy for the brochure is ready. I am sorry it has taken so long to get it out. I am sure we will not be making any amendments to it post today. Thanks for your patience The extension is not to attact new designs it is for existing designs's copy to be modified to include information from the updated copy.

medium to large companies in banking, telecom, retail etc. It will be viewed by middle and top management.

Legal

• The brochure must clearly highlight all our services without just listing as this would risk it appearing as if we have just included everything we could think of!,
Please do not do the sitting round the conference table brochure or the typical blue and white brochure.
I desperately need it to be different, unique and serious enough to show that we are capable of handling/managing all what we have included.
Our clients include the many companies starting up an office in Africa.
We are anxious to have the potential clients understand that we will help them setup under any climax/
• modern colours but not too bright. there must still be a clear serious edge to it.
• conference room table and people sitting around it.
the typical blue and white brochures often used for these type of services.

```html
<!DOCTYPE html>
<html lang="en">
<head>
<meta charset="utf-8">
<title>Ordvale – What We Do</title>
<link href="https://fonts.googleapis.com/css2?family=Great+Vibes&family=Open+Sans:ital,wght@0,400;0,600;1,700&display=swap" rel="stylesheet">
<style>
  :root {
    --olive: #546e3a;
    --sage: #b0b99c;
    --sage-light: #a9b592;
    --tagline: #a8b98a;
    --curve: #6b8050;
    --ring: #8a8a8c;
    --white: #ffffff;
    --ink: #2f3a22;
  }
  * { margin: 0; padding: 0; box-sizing: border-box; }
  html, body { width: 1200px; height: 1199px; overflow: hidden; background: var(--white); }
  .page {
    position: relative;
    width: 1200px;
    height: 1199px;
    overflow: hidden;
    background: var(--white);
    font-family: "Open Sans", Arial, sans-serif;
  }
  .pattern-band {
    position: absolute; left: 0; top: 0; width: 1200px; height: 58px;
    background: linear-gradient(90deg, #1a8a3a, #f2b51c 25%, #e5531d 50%, #1a8a3a 75%, #f2b51c);
  }
  .backdrop { position: absolute; left: 0; top: 0; }
  .lower-panel {
    position: absolute; left: 0; top: 467px; width: 1200px; height: 732px;
    background: var(--olive);
  }
  .hero-circle {
    position: absolute; left: 620px; top: -45px; width: 590px; height: 590px;
    border-radius: 50%;
    border: 5px solid var(--ring);
    background: radial-gradient(circle at 55% 55%, #8f9a8a 0%, #cfd3cc 35%, #1f6e3c 60%, #f4f4f2 80%);
  }
  .curves { position: absolute; left: 0; top: 0; pointer-events: none; }
  .section-title {
    font-family: "Great Vibes", cursive;
    font-size: 104px;
    fill: var(--white);
    stroke: var(--ink);
    stroke-width: 1.4px;
  }
  .column {
    position: absolute; top: 566px; width: 494px;
    color: var(--white); font-size: 17px; line-height: 25px; text-align: justify;
    letter-spacing: -0.15px;
    hyphens: auto;
  }
  .column-left { left: 62px; }
  .column-right { left: 622px; top: 566px; }
  .column h2 {
    font-size: 28.5px; font-style: italic; font-weight: 700;
    color: var(--sage-light); line-height: 34px; letter-spacing: -0.5px;
  }
  .column h2 .dash { font-size: 18px; font-style: normal; font-weight: 400; color: var(--white); }
  .column p + h2 { margin-top: 20px; }
  .column p + p { margin-top: 25px; }
  .column p.joined { margin-top: 0; }
  .lead {
    text-align: center; font-size: 27.5px; font-style: italic; font-weight: 700;
    color: var(--sage-light); line-height: 35px; letter-spacing: -0.3px;
    margin-bottom: 28px;
  }
  .tagline {
    position: absolute; left: 620px; top: 1003px; width: 520px;
    font-family: "Great Vibes", cursive; font-size: 62px; line-height: 68px;
    color: var(--tagline); text-align: center;
  }
</style>
</head>
<body>
<div class="page">
  <div class="pattern-band" role="img" aria-label="Woven African geometric pattern band in green, yellow, orange and black diamonds"></div>

  <svg class="backdrop" width="1200" height="467" viewBox="0 0 1200 467" aria-hidden="true">
    <polygon points="0,58 645,58 645,222 0,410" fill="var(--sage)"/>
  </svg>

  <div class="lower-panel"></div>

  <div class="hero-circle" role="img" aria-label="Illustration of business people holding a Welcome to Nigeria sign, standing on a 3D map of Nigeria in green and white"></div>

  <svg class="curves" width="1200" height="1199" viewBox="0 0 1200 1199" aria-hidden="true">
    <path d="M575 58 C 330 180, 120 380, 165 600" fill="none" stroke="var(--curve)" stroke-width="3"/>
    <path d="M600 58 C 380 200, 190 430, 225 700 C 245 860, 290 930, 300 985" fill="none" stroke="var(--curve)" stroke-width="3"/>
  </svg>

  <svg class="curves" width="1200" height="1199" viewBox="0 0 1200 1199">
    <text class="section-title" x="32" y="322" transform="rotate(-20 32 322)" textLength="590" lengthAdjust="spacingAndGlyphs">What We Do</text>
  </svg>

  <section class="column column-left">
    <h2>Services <span class="dash">–</span></h2>
    <p>Ordvale offers clients a broad spread of high value services covering Office formation, project management, cost consultancy, office setup, recruitment, training, immigration services, accommodation and much more.</p>
    <p class="joined">From startups to multinationals, companies in Lagos and other cities in Nigeria, outsource the non-core parts of their business to Ordvale.</p>
    <h2>Who hires us?</h2>
    <p>Ordvale provides managed, business services to companies in all stages of development, from early start-ups to corporations starting new in country that require a broad range of expertise to large well established corporations that simply need help completing an essential project in a hurry and on a budget.</p>
    <p>Our professionals fulfill critical roles in all stages of development and manage those functions in association with our clients. We manage the tasks and talent necessary for tactical success so you can concentrate on your strategic goals.</p>
  </section>

  <section class="column column-right">
    <p class="lead">Ordvale can provide all the front and back office support your business needs to thrive in Nigeria.</p>
    <h2>Benefit from our Economies of Scale</h2>
    <p>We buy on behalf of our many clients, so whether you need hotel rooms, car rentals or advertising services our buying power and experience ensures that it will always get the best quality services at the lowest price.</p>
    <p>Ordvale – established and well-connected in the local business community, Ordvale either owns or are partners with businesses who can provide any of the additional jigsaw pieces you need to compliment your current business operations.</p>
  </section>

  <div class="tagline">Your Local Partner<br>For Growth !!!!</div>
</div>
</body>
</html>
```